Velmora Skincare packaging designs

We are need to create packaging for our skincare brand. We need two designs. One for round jars which is for creams/capsules and the second will be for bottles/serums Some products will be larger in size so please ensure the packaging design will work and there isn't a lot white/empty space

Below are the names of some of our products.
Screw-On Top Jar (25 pads- 4 inches wide) - Glint Wipes I Skin Brightening Pads
Pump Bottle (2 oz) - ReKINDLE I Hyaluronic Acid + Vitamin Serum
Pump Bottle (6oz) - The Cloud Rinse I Conditioning Face Cleanser
Dropper bottle (1 oz) - Sunny Veil I Hydrating Moisturizer
Cream jar (1.5 oz) - Sunny Veil I Hydrating Moisturizer
Capsules Jar (25 capsules in a jar)- Lumo Burst I Moisture + Hydrating Capsules
Capsules Jar (25 capsules in a jar) - Pure Spark I Impurity Capsules

We will also need help with the packing design in terms of layout of the logo, item name, desc, and ingredients on each product.

Target Market(s)

women

Industry/Entity Type

skincare, beauty

Font styles to use
Sans Serif

Colors
E54698
E96AAD
F1A4CE
F9D9EA
FCEFF6

Requirements
Must have
• Pantone color is 2052 CP HEX #DAAFCA (218 , 175 , 202)

```html
<!DOCTYPE html>
<html lang="en">
<head>
<meta charset="UTF-8">
<title>Velmora Skincare – The Cloud Rinse Label</title>
<link href="https://fonts.googleapis.com/css2?family=Barlow+Semi+Condensed:wght@300;400;600&display=swap" rel="stylesheet">
<style>
  :root {
    --backdrop: #f1f0f0;
    --label-white: #ffffff;
    --rose: #d8708f;
    --rose-deep: #cf6486;
    --rose-light: #e08aa4;
    --ink-white: #ffffff;
    --brand-rose: #d8708f;
  }
  * { margin: 0; padding: 0; box-sizing: border-box; }
  html, body {
    width: 891px;
    height: 1200px;
    overflow: hidden;
    background: var(--backdrop);
    font-family: "Barlow Semi Condensed", sans-serif;
  }
  .canvas {
    position: relative;
    width: 891px;
    height: 1200px;
    display: flex;
    align-items: center;
    justify-content: center;
  }
  .label {
    width: 700px;
    height: 700px;
    display: flex;
    flex-direction: column;
    box-shadow: 0 2px 10px rgba(0,0,0,0.06);
  }
  .label-top {
    height: 250px;
    background: var(--label-white);
    display: flex;
    align-items: center;
    justify-content: center;
  }
  .brand-name {
    color: var(--brand-rose);
    font-weight: 400;
    font-size: 46px;
    letter-spacing: 10px;
    text-transform: uppercase;
  }
  .label-panel {
    position: relative;
    flex: 1;
    color: var(--ink-white);
    text-align: center;
  }
  .panel-texture {
    position: absolute;
    inset: 0;
    background: radial-gradient(ellipse at 40% 40%, var(--rose-light) 0%, var(--rose) 55%, var(--rose-deep) 100%);
  }
  .panel-content {
    position: relative;
    padding-top: 92px;
    display: flex;
    flex-direction: column;
    align-items: center;
  }
  .product-name {
    font-weight: 600;
    font-size: 54px;
    letter-spacing: 2px;
    line-height: 1;
    text-transform: uppercase;
  }
  .divider {
    width: 360px;
    height: 2px;
    background: var(--ink-white);
    margin: 18px 0 16px;
  }
  .product-desc {
    font-weight: 300;
    font-size: 22px;
    letter-spacing: 6px;
    text-transform: uppercase;
  }
  .product-size {
    margin-top: 150px;
    font-weight: 400;
    font-size: 22px;
    letter-spacing: 2px;
    text-transform: uppercase;
  }
</style>
</head>
<body>
  <main class="canvas">
    <section class="label">
      <header class="label-top">
        <span class="brand-name">Velmora</span>
      </header>
      <div class="label-panel">
        <div class="panel-texture" role="img" aria-label="Soft rose background with a fine topographic contour line pattern"></div>
        <div class="panel-content">
          <h1 class="product-name">The Cloud Rinse</h1>
          <div class="divider"></div>
          <p class="product-desc">Conditioning Face Cleanser</p>
          <p class="product-size">6oz</p>
        </div>
      </div>
    </section>
  </main>
</body>
</html>
```